I have a PHP web application to manage IT support calls and require a front-end design and user logon screen.

I have attached the current design which needs improving.

I have 2 current designs. The 2nd design is one I have been working on but requires a "professional touch". I also require the tables designed with dummy data from the 1st design.

I have attached my company logo in AI format which I would like incorporated into the design. There should also be a placeholder to supply the users company name upon login.

The screenshots I have attached should explain what I am looking for.

The Home Page should include charts which show statistical information such as:
Number of support tickets logged per month. Bar Chart etc.
Number of currently open support tickets.
Number of Quote Requests awaiting a response.
Number of Files and file repository.
Number of Reports.
Number of Customers.

For the Jobs and Customers pages the table fields should be designed as per the attached screenshots but a better looking tables. The table options such as uploading a file and adding a customer - these options can be changed and displayed differently.

Quotes page should display quotes returned and a "request a quote form".

Files page should have a good structure for browsing through an archive of files.

Profile page should have the option to include a profile picture.

An additional side page should be created for a web based calendar (these calendar entries will be updated by code).

The navbar should also include an alerts section.
The current attached design I have is based on bootstraps navbar.

Inspiration: http://plenvaro.com/freebie/free-admin-templates-for-backend-panels/

Hopefully this above link will show you some navigation style designs that I am looking for.

Please note, I will be doing the PHP coding myself and it is just the page designs I require in either HTML and or PHP format. I also require the CSS files for this project.
I need the code in a format where I can add and remove items in the menu from the code and not PSD/image based format.

If you think this project requires a higher budget let me know what you would expect and I will increase it!

Any questions, please let me know.
Dummy data can be shown for design purposes.

I have provided you a dummy login to our current system to show you the system:
https://reef.vomilbrixtonsolutions.co.uk/
username: dan.hollow@vomilbrixtonsolutions.co.uk
password:K#72zqTm

```html
<!DOCTYPE html>
<html lang="en">
<head>
<meta charset="utf-8">
<title>Vomil Brixton Solutions – Dashboard</title>
<link href="https://fonts.googleapis.com/css2?family=Open+Sans:wght@400;600;700&display=swap" rel="stylesheet">
<style>
:root{
  --blue:#1f4c9f;
  --blue-dark:#1a418a;
  --side:#2e2e2e;
  --side-line:#3c3c3c;
  --side-active:#474747;
  --head-grey:#595959;
  --red:#f04f52;
  --green:#4cd263;
  --cyan:#2ec6dd;
  --text:#444;
  --muted:#8a8a8a;
  --line:#e3e3e3;
  --bg:#f6f6f6;
}
*{box-sizing:border-box;margin:0;padding:0}
html,body{width:1026px;height:1200px;overflow:hidden}
body{font-family:"Open Sans",Arial,sans-serif;color:var(--text);background:var(--bg);position:relative;font-size:11px}
.sidebar{position:absolute;left:0;top:0;width:178px;height:1161px;background:var(--side)}
.brand{height:84px;background:var(--blue);display:flex;align-items:center;padding-left:22px;gap:8px;color:#fff}
.brand-dot{width:34px;height:34px;border-radius:50%;border:2px solid #fff}
.brand-name{font-size:20px;font-weight:700;letter-spacing:.5px}
.nav a{display:flex;align-items:center;height:33px;padding-left:20px;color:#fff;text-decoration:none;font-size:11px;border-bottom:1px solid var(--side-line);gap:14px}
.nav a.active{background:var(--side-active)}
.nav svg{width:15px;height:15px;fill:#fff}
.topbar{position:absolute;left:178px;top:0;width:848px;height:47px;background:#fff;border-bottom:1px solid #ddd;display:flex;align-items:center;padding-left:20px}
.topbar .title{font-size:12px;color:#333;display:flex;gap:7px;align-items:center}
.alerts{position:absolute;left:522px;top:12px;display:flex;gap:15px}
.alert{position:relative;width:16px;height:18px}
.alert svg{width:14px;height:14px;fill:#222;position:absolute;bottom:0}
.badge{position:absolute;left:8px;top:-4px;width:13px;height:13px;border-radius:50%;font-size:8px;color:#fff;text-align:center;line-height:13px}
.user{position:absolute;left:683px;top:10px;display:flex;align-items:center;gap:6px;font-size:12px;color:#333}
.avatar{width:27px;height:27px;border-radius:50%;background:linear-gradient(#caa487,#6d5140)}
.user .count{margin-left:14px;background:var(--blue);color:#fff;font-size:10px;width:15px;height:15px;text-align:center;line-height:15px}
.panel{position:absolute;background:#fff;border:1px solid var(--line)}
.panel-head{height:39px;display:flex;align-items:center;padding-left:13px;gap:8px;color:#fff;font-weight:700;font-size:12px;text-transform:uppercase}
.panel-head.blue{background:var(--blue)}
.panel-head.grey{background:var(--head-grey)}
.panel-head svg{width:17px;height:17px;fill:#fff}
.tabs{margin-left:auto;margin-right:12px;display:flex;gap:4px}
.tabs span{background:#fff;color:#333;font-size:8px;font-weight:400;padding:1px 3px;text-transform:none;border:1px solid #999}
.chart-box{margin:8px 10px;border:1px solid var(--line);height:200px}
.job-stats{display:flex;justify-content:space-around;padding:20px 12px 0;height:100px;border-bottom:1px solid var(--line);margin:0 12px}
.job-stat{text-align:center;font-size:8px;color:#555}
.job-stat svg{display:block;margin:0 auto 6px}
.donut-row{display:flex;align-items:center;padding:10px 14px}
.legend{margin-left:22px}
.legend div{display:flex;align-items:center;gap:8px;font-size:10px;color:#333;margin-bottom:11px}
.pill{width:20px;height:16px;border-radius:8px;color:#fff;font-size:8px;text-align:center;line-height:16px}
.gauge{position:absolute;top:359px;width:110px;text-align:center;font-size:11.5px;color:#333}
.gauge svg{display:block;margin:8px auto 0}
.stat{position:absolute;width:83px;height:48px;background:#fff;border:1px solid #ddd;padding:7px 10px;color:var(--muted);font-size:11px}
.stat b{display:flex;align-items:center;gap:3px;color:#555;font-size:12px;font-weight:600;margin-top:1px}
.ic{width:10px;height:10px;border-radius:50%;display:inline-block;position:relative}
.ic::after{content:"";position:absolute;left:3px;top:2px;border:2px solid transparent}
.ic.up::after{border-bottom:4px solid #fff;top:0}
.ic.down::after{border-top:4px solid #fff;top:4px}
.proj{height:73px;border-bottom:1px solid #e8e8e8;background:#f7f7f7;padding:12px 12px 0 12px;font-size:12px;color:#555}
.box{display:inline-block;width:9px;height:9px;border:1px solid #888;border-radius:2px;margin-right:5px;vertical-align:-1px;background:#fff}
.proj small{display:block;font-size:11px;color:var(--muted);padding-left:16px;margin-top:3px}
.bar{margin:8px 0 0 28px;width:204px;height:4px;background:#e9e9e9;border-radius:2px}
.bar i{display:block;height:4px;width:58%;border-radius:2px}
.panel-foot{position:absolute;left:0;right:0;bottom:0;height:40px;border-top:1px solid var(--line);display:flex;align-items:center;padding:0 10px;justify-content:space-between;font-size:10.5px;color:#777}
.btn{color:#fff;font-size:11px;font-weight:600;padding:5px 15px;border-radius:2px}
.btn.dark{background:linear-gradient(#6a6a6a,#4a4a4a)}
.btn.blue{background:var(--blue)}
.input{border:1px solid #ddd;height:28px;width:100px;padding:0 8px;line-height:26px;color:#aaa;font-size:11px}
.msg{position:absolute;display:flex;gap:10px}
.face{width:40px;height:40px;border-radius:50%;border:2px solid #eee;background:linear-gradient(#b8977c,#4e3a2e)}
.bubble{border:1px solid #ddd;border-radius:3px;padding:8px 10px;font-size:9px;color:#555;width:196px;line-height:1.6}
.bubble .meta{display:flex;justify-content:space-between;font-size:8.5px;color:#888;margin-bottom:3px}
.task{margin:0 8px 7px;height:27px;border:1px solid #e3e3e3;display:flex;align-items:center;padding-left:10px;font-size:11px;color:#555;position:relative}
.task::before{content:"";position:absolute;left:-1px;top:-1px;bottom:-1px;width:3px;background:#555}
table{width:100%;border-collapse:collapse;font-size:11px;color:#666;text-align:center}
th{height:29px;font-weight:600;color:#333;font-size:11.5px;border-right:1px solid #e5e5e5;border-bottom:1px solid #e5e5e5}
td{height:25.6px;border-right:1px solid #e9e9e9;border-bottom:1px solid #e9e9e9}
th:last-child,td:last-child{border-right:0}
.chev{display:inline-block;width:7px;height:7px;border-left:1.5px solid #bbb;border-top:1.5px solid #bbb;transform:rotate(45deg);margin-top:3px}
.chev.dn{transform:rotate(225deg);margin-top:-3px}
.pager{display:flex}
.pager span{border:1px solid #ddd;width:27px;height:27px;text-align:center;line-height:25px;color:#333;margin-left:-1px}
.contact{margin:0 8px 9px;height:38px;border:1px solid #e3e3e3;display:flex;align-items:center;padding:0 6px;gap:10px}
.contact .face{width:27px;height:27px;border:0}
.contact b{display:block;font-weight:400;font-size:12px;color:#333}
.contact small{font-size:9px;color:#444}
.acts{margin-left:auto;display:flex;gap:6px}
.acts i{width:21px;height:21px;border-radius:50%;display:block}
.footer{position:absolute;left:0;top:1161px;width:1026px;height:39px;background:#232323;color:#fff;display:flex;align-items:center;justify-content:space-between;padding:0 24px;font-size:11px}
.footer nav{display:flex;gap:7px}
.footer nav span{color:#bbb}
</style>
</head>
<body>

<aside class="sidebar">
  <div class="brand"><span class="brand-dot"></span><span class="brand-name">VOMIL</span></div>
  <nav class="nav">
    <a class="active" href="#"><svg viewBox="0 0 16 16"><path d="M8 1 1 8h2v7h4v-4h2v4h4V8h2z"/></svg>Home</a>
    <a href="#"><svg viewBox="0 0 16 16"><path d="M2 3l2-2 11 11-2 2zM13 1l2 2-11 11-2-2z"/></svg>Jobs</a>
    <a href="#"><svg viewBox="0 0 16 16"><circle cx="8" cy="5" r="3.5"/><path d="M2 15c0-4 3-6 6-6s6 2 6 6z"/></svg>Customers</a>
    <a href="#"><svg viewBox="0 0 16 16"><path d="M2 6h12v8H2zM3 2h10v3H3z"/></svg>Inventory</a>
    <a href="#"><svg viewBox="0 0 16 16"><path d="M1 5l7-4 7 4v9H1zM3 6l5 3 5-3"/></svg>Reports</a>
    <a href="#"><svg viewBox="0 0 16 16"><path d="M1 3h4v12H1zM6 3h4v12H6zM11 3h4v12h-4z"/></svg>Files</a>
    <a href="#"><svg viewBox="0 0 16 16"><circle cx="9" cy="6" r="5"/><path d="M1 15c0-3 2-5 5-5v5z"/></svg>Quotes</a>
  </nav>
</aside>

<header class="topbar">
  <div class="title"><svg width="15" height="13" viewBox="0 0 15 13"><rect x="1" y="1" width="13" height="9" fill="none" stroke="#1f4c9f" stroke-width="1.5"/><rect x="5" y="11" width="5" height="1.5" fill="#1f4c9f"/></svg>Dashboard</div>
  <div class="alerts">
    <div class="alert"><svg viewBox="0 0 14 14"><circle cx="7" cy="4" r="3"/><path d="M1 14c0-4 3-5 6-5s6 1 6 5z"/></svg><span class="badge" style="background:var(--blue)">6</span></div>
    <div class="alert"><svg viewBox="0 0 14 14"><path d="M7 1c3 0 4 2 4 5v4l2 2H1l2-2V6c0-3 1-5 4-5zM5 13h4a2 2 0 0 1-4 0z"/></svg><span class="badge" style="background:var(--red)">6</span></div>
    <div class="alert"><svg viewBox="0 0 14 14"><path d="M0 3h14v9H0zM1 4l6 4 6-4"/></svg><span class="badge" style="background:var(--green)">6</span></div>
  </div>
  <div class="user"><span class="avatar" role="img" aria-label="Profile photo of the signed-in user"></span>Fernando<span class="count">6</span><span style="border:4px solid transparent;border-top-color:#aaa;margin-top:4px"></span></div>
</header>

<!-- Latest report -->
<section class="panel" style="left:192px;top:66px;width:490px;height:259px">
  <div class="panel-head blue"><svg viewBox="0 0 16 16"><path d="M1 1h1.5v13H15v1.5H1z"/><path d="M4 8h2v5H4zM7 5h2v8H7zM10 9h2v4h-2zM12 3h2v10h-2z"/></svg>Latest Report
    <div class="tabs"><span>Visitors</span><span>Revenue</span><span>Growth</span></div></div>
  <div class="chart-box">
    <svg width="468" height="198" viewBox="0 0 470 215">
      <g stroke="#eee" stroke-width="1">
        <line x1="30" y1="10" x2="455" y2="10"/><line x1="30" y1="55" x2="455" y2="55"/><line x1="30" y1="100" x2="455" y2="100"/><line x1="30" y1="145" x2="455" y2="145"/><line x1="30" y1="190" x2="455" y2="190"/>
        <line x1="30" y1="10" x2="30" y2="190"/><line x1="128" y1="10" x2="128" y2="190"/><line x1="226" y1="10" x2="226" y2="190"/><line x1="324" y1="10" x2="324" y2="190"/><line x1="455" y1="10" x2="455" y2="190"/>
      </g>
      <g font-size="8" fill="#999" font-family="Open Sans,sans-serif">
        <text x="14" y="13">8</text><text x="14" y="58">6</text><text x="14" y="103">4</text><text x="14" y="148">2</text><text x="14" y="193">0</text>
        <g text-anchor="middle"><text x="30" y="207">0</text><text x="62.7" y="207">1</text><text x="95.4" y="207">2</text><text x="128.1" y="207">3</text><text x="160.8" y="207">4</text><text x="193.5" y="207">5</text><text x="226.2" y="207">6</text><text x="258.8" y="207">7</text><text x="291.5" y="207">8</text><text x="324.2" y="207">9</text><text x="356.9" y="207">10</text><text x="389.6" y="207">11</text><text x="422.3" y="207">12</text><text x="455" y="207">13</text></g>
      </g>
      <rect x="384" y="20" width="6" height="6" fill="#2ec6dd"/><text x="392" y="26" font-size="6" fill="#aaa">Revenue</text>
      <rect x="420" y="20" width="6" height="6" fill="#4cd263"/><text x="428" y="26" font-size="6" fill="#aaa">Profit</text>
      <path d="M30 100L62.7 111.25L95.4 95.5L128.1 66.25L160.8 79.75L193.5 77.5L226.2 70.75L258.8 55L291.5 70.75L324.2 100L356.9 100L389.6 88.75L422.3 77.5L455 100V190H30Z" fill="#2ec6dd" fill-opacity=".12"/>
      <path d="M30 145L62.7 156.25L95.4 140.5L128.1 111.25L160.8 124.75L193.5 122.5L226.2 115.75L258.8 100L291.5 115.75L324.2 145L356.9 145L389.6 133.75L422.3 122.5L455 145V190H30Z" fill="#4cd263" fill-opacity=".12"/>
      <polyline points="30,100 62.7,111.25 95.4,95.5 128.1,66.25 160.8,79.75 193.5,77.5 226.2,70.75 258.8,55 291.5,70.75 324.2,100 356.9,100 389.6,88.75 422.3,77.5 455,100" fill="none" stroke="#2ec6dd" stroke-width="1.3"/>
      <polyline points="30,145 62.7,156.25 95.4,140.5 128.1,111.25 160.8,124.75 193.5,122.5 226.2,115.75 258.8,100 291.5,115.75 324.2,145 356.9,145 389.6,133.75 422.3,122.5 455,145" fill="none" stroke="#4cd263" stroke-width="1.3"/>
      <g fill="#fff" stroke="#2ec6dd" stroke-width="1.3"><circle cx="30" cy="100" r="2.5"/><circle cx="62.7" cy="111.25" r="2.5"/><circle cx="95.4" cy="95.5" r="2.5"/><circle cx="128.1" cy="66.25" r="2.5"/><circle cx="160.8" cy="79.75" r="2.5"/><circle cx="193.5" cy="77.5" r="2.5"/><circle cx="226.2" cy="70.75" r="2.5"/><circle cx="258.8" cy="55" r="2.5"/><circle cx="291.5" cy="70.75" r="2.5"/><circle cx="324.2" cy="100" r="2.5"/><circle cx="356.9" cy="100" r="2.5"/><circle cx="389.6" cy="88.75" r="2.5"/><circle cx="422.3" cy="77.5" r="2.5"/><circle cx="455" cy="100" r="2.5"/></g>
      <g fill="#fff" stroke="#4cd263" stroke-width="1.3"><circle cx="30" cy="145" r="2.5"/><circle cx="62.7" cy="156.25" r="2.5"/><circle cx="95.4" cy="140.5" r="2.5"/><circle cx="128.1" cy="111.25" r="2.5"/><circle cx="160.8" cy="124.75" r="2.5"/><circle cx="193.5" cy="122.5" r="2.5"/><circle cx="226.2" cy="115.75" r="2.5"/><circle cx="258.8" cy="100" r="2.5"/><circle cx="291.5" cy="115.75" r="2.5"/><circle cx="324.2" cy="145" r="2.5"/><circle cx="356.9" cy="145" r="2.5"/><circle cx="389.6" cy="133.75" r="2.5"/><circle cx="422.3" cy="122.5" r="2.5"/><circle cx="455" cy="145" r="2.5"/></g>
    </svg>
  </div>
</section>

<!-- Job -->
<section class="panel" style="left:704px;top:66px;width:281px;height:259px">
  <div class="panel-head grey"><svg viewBox="0 0 16 16"><path d="M1 5h14v9H1zM5 2h6v3H9.5V3.5h-3V5H5z"/></svg>Job</div>
  <div class="job-stats">
    <div class="job-stat"><svg width="52" height="28"><g fill="#f04f52"><rect x="0" y="14" width="3" height="14"/><rect x="5" y="8" width="3" height="20"/><rect x="10" y="18" width="3" height="10"/><rect x="15" y="4" width="3" height="24"/><rect x="20" y="12" width="3" height="16"/><rect x="25" y="0" width="3" height="28"/><rect x="30" y="10" width="3" height="18"/><rect x="35" y="6" width="3" height="22"/><rect x="40" y="14" width="3" height="14"/><rect x="45" y="9" width="3" height="19"/></g></svg>1200 Visitors</div>
    <div class="job-stat"><svg width="52" height="28"><g fill="#4cd263"><rect x="0" y="16" width="3" height="12"/><rect x="5" y="8" width="3" height="20"/><rect x="10" y="18" width="3" height="10"/><rect x="15" y="6" width="3" height="22"/><rect x="20" y="14" width="3" height="14"/><rect x="25" y="2" width="3" height="26"/><rect x="30" y="10" width="3" height="18"/><rect x="35" y="0" width="3" height="28"/><rect x="40" y="12" width="3" height="16"/><rect x="45" y="7" width="3" height="21"/></g></svg>5000 Members</div>
    <div class="job-stat"><svg width="52" height="28"><g fill="#2ec6dd"><rect x="0" y="14" width="3" height="14"/><rect x="5" y="6" width="3" height="22"/><rect x="10" y="16" width="3" height="12"/><rect x="15" y="4" width="3" height="24"/><rect x="20" y="12" width="3" height="16"/><rect x="25" y="0" width="3" height="28"/><rect x="30" y="10" width="3" height="18"/><rect x="35" y="5" width="3" height="23"/><rect x="40" y="13" width="3" height="15"/><rect x="45" y="8" width="3" height="20"/></g></svg>8000 Bounce</div>
  </div>
  <div class="donut-row">
    <svg width="112" height="112" viewBox="0 0 112 112"><g transform="rotate(-90 56 56)" fill="none" stroke-width="20">
      <circle cx="56" cy="56" r="45" stroke="#f04f52" stroke-dasharray="110 173"/>
      <circle cx="56" cy="56" r="45" stroke="#4cd263" stroke-dasharray="0 110 125 48"/>
      <circle cx="56" cy="56" r="45" stroke="#2ec6dd" stroke-dasharray="0 235 48 0"/>
    </g></svg>
    <div class="legend">
      <div><span class="pill" style="background:var(--red)">5</span>Today's Revenue</div>
      <div><span class="pill" style="background:var(--green)">8</span>Yesterday's Profit</div>
      <div><span class="pill" style="background:var(--cyan)">4</span>Monday's Visitors</div>
    </div>
  </div>
</section>

<!-- Gauges -->
<div class="gauge" style="left:185px">Today's Visitors<svg width="84" height="84" viewBox="0 0 84 84"><circle cx="42" cy="42" r="39" fill="#fff" stroke="#e5e5e5" stroke-width="3"/><circle cx="42" cy="42" r="39" fill="none" stroke="#1f4c9f" stroke-width="3" stroke-dasharray="150 95" transform="rotate(145 42 42)"/><text x="42" y="48" text-anchor="middle" font-size="16" fill="#1f4c9f">85</text></svg></div>
<div class="gauge" style="left:316px">Customers<svg width="84" height="84" viewBox="0 0 84 84"><circle cx="42" cy="42" r="39" fill="#fff" stroke="#e5e5e5" stroke-width="3"/><circle cx="42" cy="42" r="39" fill="none" stroke="#2ec6dd" stroke-width="3" stroke-dasharray="105 140" transform="rotate(165 42 42)"/><text x="42" y="48" text-anchor="middle" font-size="16" fill="#2ec6dd">65</text></svg></div>
<div class="gauge" style="left:446px">Reports<svg width="84" height="84" viewBox="0 0 84 84"><circle cx="42" cy="42" r="39" fill="#fff" stroke="#e5e5e5" stroke-width="3"/><circle cx="42" cy="42" r="39" fill="none" stroke="#f04f52" stroke-width="3" stroke-dasharray="75 170" transform="rotate(165 42 42)"/><text x="42" y="48" text-anchor="middle" font-size="16" fill="#f04f52">35</text></svg></div>
<div class="gauge" style="left:577px">Quotes<svg width="84" height="84" viewBox="0 0 84 84"><circle cx="42" cy="42" r="39" fill="#fff" stroke="#e5e5e5" stroke-width="3"/><circle cx="42" cy="42" r="39" fill="none" stroke="#4cd263" stroke-width="3" stroke-dasharray="120 125" transform="rotate(165 42 42)"/><text x="42" y="48" text-anchor="middle" font-size="16" fill="#4cd263">75</text></svg></div>

<!-- Stat boxes -->
<div class="stat" style="left:704px;top:354px">Profit<b>$50,000 <i class="ic up" style="background:var(--green)"></i></b></div>
<div class="stat" style="left:804px;top:354px">Reports<b>55.89% <i class="ic down" style="background:var(--red)"></i></b></div>
<div class="stat" style="left:904px;top:354px">Customers<b>11,000 <i class="ic up" style="background:var(--cyan)"></i></b></div>
<div class="stat" style="left:704px;top:421px">Bounce Rate<b>30.07% <i class="ic down" style="background:var(--cyan)"></i></b></div>
<div class="stat" style="left:804px;top:421px">Visitors<b>25,000 <i class="ic up" style="background:var(--green)"></i></b></div>
<div class="stat" style="left:904px;top:421px">Oders<b>5,000 <i class="ic down" style="background:var(--red)"></i></b></div>

<!-- Projects -->
<section class="panel" style="left:191px;top:504px;width:264px;height:295px">
  <div class="panel-head grey"><svg viewBox="0 0 16 16"><path d="M1 2h14v10H1zM2.5 3.5v7h11v-7zM5 13h6v1.5H5z"/></svg>Projects</div>
  <div class="proj"><span class="box"></span>Hospital Management System<small>Due : 26/2/2012 - 80% Done</small><div class="bar"><i style="background:var(--blue)"></i></div></div>
  <div class="proj"><span class="box"></span>Question and Answers Script<small>Due : 26/2/2012 - 80% Done</small><div class="bar"><i style="background:var(--red)"></i></div></div>
  <div class="proj"><span class="box"></span>Software Downloads Script<small>Due : 26/2/2012 - 80% Done</small><div class="bar"><i style="background:var(--cyan)"></i></div></div>
  <div class="panel-foot">Last Update - 55 mins ago<span class="btn dark">Refresh</span></div>
</section>

<!-- Chats -->
<section class="panel" style="left:463px;top:504px;width:265px;height:295px">
  <div class="panel-head blue"><svg viewBox="0 0 16 16"><path d="M1 2h10v7H5l-3 3V9H1zM12 5h3v7h-1v2l-2-2H6v-2h6z"/></svg>Chats</div>
  <div class="msg" style="left:8px;top:61px"><span class="face" role="img" aria-label="Chat participant photo"></span><div class="bubble"><div class="meta"><span>Ashok</span><span>4 hours ago</span></div>Vivamus diam elit diam, consectetur dapibus adipiscing elit.</div></div>
  <div class="msg" style="left:9px;top:160px"><div class="bubble" style="width:196px"><div class="meta"><span>3 hours ago</span><span>Ravi</span></div>Vivamus diam elit diam, consectetur fconsectetur dapibus adipiscing elit.</div><span class="face" role="img" aria-label="Chat participant photo"></span></div>
  <div class="panel-foot"><span class="input">Message...</span><span class="btn blue" style="padding:5px 22px">Send</span></div>
</section>

<!-- Tasks -->
<section class="panel" style="left:735px;top:504px;width:265px;height:295px">
  <div class="panel-head grey" style="margin-bottom:8px"><svg viewBox="0 0 16 16"><path d="M1 3h14v12H1zM2.5 6v7.5h11V6zM4 1h1.5v3H4zM10.5 1H12v3h-1.5z"/></svg>Tasks</div>
  <div class="task"><span class="box"></span>Lorem ipsum dolor sit amet,</div>
  <div class="task"><span class="box"></span>consectetur adipisicing elit, sed do</div>
  <div class="task"><span class="box"></span>eiusmod tempor incididunt ut labore et</div>
  <div class="task"><span class="box"></span>dolore magna aliqua. Ut enim ad minim</div>
  <div class="task"><span class="box"></span>veniam, quis nostrud exercitation</div>
  <div class="task"><span class="box"></span>ullamco laboris nisi ut aliquip ex ea</div>
  <div class="panel-foot"><span class="input" style="width:110px">Enter Task here...</span><span class="btn dark">Add Task</span></div>
</section>

<!-- Pages -->
<section class="panel" style="left:192px;top:828px;width:506px;height:283px">
  <div class="panel-head blue"><svg viewBox="0 0 16 16"><path d="M2 1h8l3 3v5h-1.5V5H9V2.5H3.5v11H8V15H2z"/><circle cx="12" cy="12" r="3.5"/></svg>Pages</div>
  <table>
    <tr><th style="width:46px"><span class="box" style="margin:0"></span></th><th>PAGE TITLE</th><th>FILE SIZE</th><th>STATUS</th><th>SORT</th><th>ACTION</th></tr>
    <tr><td><span class="box" style="margin:0"></span></td><td>About Us</td><td>253.4 KB</td><td>R</td><td><i class="chev"></i></td><td></td></tr>
    <tr><td><span class="box" style="margin:0"></span></td><td>Contact Us</td><td>213 KB</td><td>A</td><td><i class="chev dn"></i></td><td></td></tr>
    <tr><td><span class="box" style="margin:0"></span></td><td>Dashboard</td><td>1.24 MB</td><td>P</td><td><i class="chev"></i></td><td></td></tr>
    <tr><td><span class="box" style="margin:0"></span></td><td>Download</td><td>30.00 MB</td><td>R</td><td><i class="chev dn"></i></td><td></td></tr>
    <tr><td><span class="box" style="margin:0"></span></td><td>Portfolio</td><td>140 MB</td><td>A</td><td><i class="chev"></i></td><td></td></tr>
    <tr><td><span class="box" style="margin:0"></span></td><td>Contact Us</td><td>213 KB</td><td>P</td><td><i class="chev dn"></i></td><td></td></tr>
    <tr><td><span class="box" style="margin:0"></span></td><td>Dashboard</td><td>1.24 MB</td><td>R</td><td><i class="chev"></i></td><td></td></tr>
  </table>
  <div class="panel-foot" style="height:41px"><span style="display:flex;gap:14px;align-items:center"><span class="input">Add new page</span><span class="btn blue" style="padding:5px 10px">Delete All</span></span><span class="pager"><span>1</span><span>2</span><span>3</span><span>4</span><span>...</span></span></div>
</section>

<!-- Contacts -->
<section class="panel" style="left:709px;top:828px;width:291px;height:283px">
  <div class="panel-head grey" style="margin-bottom:10px"><svg viewBox="0 0 16 16"><path d="M1 6c0-3 14-3 14 0v2h-4V6.5h-6V8H1zM3 9h10l1 6H2z"/></svg>Contacts</div>
  <div class="contact"><span class="face" role="img" aria-label="Contact photo"></span><div><b>Jasica</b><small>(+1) 123 456 7890</small></div><div class="acts"><i style="background:var(--red)"></i><i style="background:var(--cyan)"></i><i style="background:var(--green)"></i></div></div>
  <div class="contact"><span class="face" role="img" aria-label="Contact photo"></span><div><b>Jhon</b><small>(+1) 123 456 7890</small></div><div class="acts"><i style="background:var(--red)"></i><i style="background:var(--cyan)"></i><i style="background:var(--green)"></i></div></div>
  <div class="contact"><span class="face" role="img" aria-label="Contact photo"></span><div><b>Jasica</b><small>(+1) 123 456 7890</small></div><div class="acts"><i style="background:var(--red)"></i><i style="background:var(--cyan)"></i><i style="background:var(--green)"></i></div></div>
  <div class="contact"><span class="face" role="img" aria-label="Contact photo"></span><div><b>Jhon</b><small>(+1) 123 456 7890</small></div><div class="acts"><i style="background:var(--red)"></i><i style="background:var(--cyan)"></i><i style="background:var(--green)"></i></div></div>
  <div class="panel-foot" style="height:41px;color:#444;font-size:11px">536 Contacts<span class="btn dark">Add New Contacts</span></div>
</section>

<footer class="footer">
  <span>Copy rigthe 2014 ©. Vomil Brixton Solutions Ltd. All rights reserved</span>
  <nav>Home<span>|</span>Jobs<span>|</span>Customers<span>|</span>Inventory<span>|</span>Reports<span>|</span>Files<span>|</span>Quotes</nav>
</footer>

</body>
</html>
```